Our Almond Vosk needs new labels and logo as good as the product itself - the ultimate nut milk

What we do:
We are a cold-pressed Almond milk company. Our Vosk (nut milk) is as pure as can be - Nuts, water, salt - that's it. Our current design is good but it's not telling people why they should spend more on our product than the competitors.

What we need:
We would like to have improved designs (or totally new designs!) for:
Our Front and Back labels on our bottles
Our Logo (currently the same as the logo on the bottle but we're very happy to change it.

The key thing is to accentuate the words "Almond Vosk" over "Plainly Fine" and to include the words "Cold-Pressed).

We're interested in both totally new designs and updates of our current design.

What we make:
Our Vosk is totally unique in UK and Ireland. The advantages of our Vosk over other non-dairy milks are:
1. Cold-pressed (we use cold-press and HPP technology so our product is never heated - keeps all the nutrients, flavour and creamy texture - all other UK/Ireland non-dairy milks are UHT)
2. Our nuts are activated before we press which increases the nutrient value in the Vosk
3. 10% Nuts (most almond milks have around 1-2%)
4. It's naturally creamy and delicious
5. We never use refined sugars (we only ever sweeten with dates), emulsifiers, flavourings, preservatives or any other nasties.
6. The ingredients list is so Plain it's good!

What we want to change:
The feedback we're getting from retailers and industry is that our brand name (Plainly Fine) is too prominent on the label and that Almond Vosk (ie what the product actually is) isn't prominent enough. Vosk is our trademarked name so we want to make more of it and have Almond Vosk much bigger on the label. We're contemplating having Plainly Fine as the strap line or just as the brand name but smaller than Almond Vosk. We also need to have the words "Cold-Pressed" on the front label to justify the premium price.

We need a front and a back label which is going to stand out on the fridge shelf as totally different and premium. At the moment we use an almond shaped label (see upload) that is a different colour for each of the flavours (Original (dark Brown), Slightly Sweetened (light brown), Strawberry (bright pink), Mango (bright orange). We like having two labels as they allow the creamy look and colour of the Vosk to show through the bottle (we don't want to cover it up). Our Original and Slightly Sweetened comes in 750ml (which look like old-fashioned milk bottles) and 330ml bottles, the flavours come in 250ml - at the moment we use the same label size for all different sizes but we're willing to change that if it looks better. We don't want a wrap around label. We currently have almond shaped labels which we like but we are willing to change if it looks good. Most of our competitors are in tetra pack. A couple are in opaque bottles so we like our bottle to show off the product.

The Original and Slightly Sweetened are the most important to get right as they are the genuine milk alternatives. The flavours are a secondary line of grab and go drinks so not the main focus of the brand.

We're about to go into more mainstream shops so we need the bottles to speak for themselves more. Until now we've been in shops where consumers are more likely to turn the bottle around and read the differences for themselves. Now we need the bottle to sell itself a bit more.

We're happy to totally shake up the label and branding if that's what works!

The Details:

Information that needs to be on each label:
Front Label:
Plainly Fine Almond Vosk (Or Almond Vosk Plainly Fine)
Cold-Pressed
Activated
750ml/330ml/250ml
Flavour (Original, Slightly Sweetened, Strawberry, Mango)

Back Label:
List of ingredients - we'd like to make this more front and centre to show how simple the product is (like naked bars) - for the Original version this is: Almonds, Water, Pink Himalayan Salt.
I'm Bored give me a shake
Separation is Natural
barcode
Nutritional panel
A blend of Almonds and water (this is our legal name so has to be on there somewhere)
Cold-pressed, cold-pressured
Our address: Tamblin Foods, 9 Fenwick Street, Armagh, BT62 4RX
facebook, twitter and instagram logos and our handle ItsPlainlyFine
Our website: ItsPlainlyFine.example
Keep chilled below 4degrees Celsius (or shortened to c)
Use within 3 days of opening
Vegan symbol
Use by date: see lid

Space Available for the labels:
750ml: 235mm circumference, 95mm high
330ml:185mm circumference, 85mm high
250ml: 165mm circumference, 75mm high

Our Brand Identity:
Our brand is all about being healthy without compromising taste or nutrients. We cold-press our product so it tastes better and retains more of its nutrients. We are scrupulously honest - what you see is what you get. We are quite playful with a tongue in cheek humour so happy to see fun ideas. We like to use the term Plain as a good thing! We're a premium brand that is basically the best that you can buy without making it yourself!

Other things that are true about our product that you could play around with or just to give you a feel for the product:
Works just like Milk
Just Nuts
No refined sugars
Nothing artificial
contains Nuts (loads of them)
Never heated
Creamy and delicious
Dairy-free
Soy-Free
Raw, Spanish Almonds
Activated Almonds

Our Logo is currently just the words "Plainly Fine" the same as our label but what the logo is going forward will depend on the new labels. We'd like to create an improved logo around the same lines as the new labels.

Target Market(s)

Plant-Based, Premium, healthy eating, free-from, dairy-free, millenials. vegan

Industry/Entity Type

Food Production

Colors

Designer to choose colors to be used in the design.

Requirements
Must have
• More prominence for "Almond Vosk" and less prominence for "Plainly Fine".
• The words "cold-pressed" on the front of the label.
• See project description for the information we need on the back of the label
Nice to have
• Modern, bold, stand out designs that are both premium and approachable. A bit more artisan than mass-produced but modern not twee.
Should not have
• should not be something that looks like other things on the shelf. Shouldn't look too mass produced or tacky.

```html
<!DOCTYPE html>
<html lang="en">
<head>
<meta charset="utf-8">
<title>Almond Vosk – Front Label</title>
<link rel="stylesheet" href="https://fonts.googleapis.com/css2?family=Oswald:wght@600&family=Yesteryear&display=swap">
<style>
  :root {
    --backdrop: #e4e4e4;
    --leaf-green: #9dd68a;
    --forest: #0a6644;
    --forest-deep: #07553a;
    --badge: #0a3b29;
    --almond-light: #dcb27f;
    --almond: #c49a68;
    --almond-edge: #a47b4c;
    --cream: #ffffff;
    --cocoa: #2a1c13;
  }
  html, body {
    margin: 0;
    padding: 0;
    overflow: hidden;
  }
  body {
    width: 1114px;
    height: 1200px;
    background: var(--backdrop);
    display: flex;
    align-items: center;
    justify-content: center;
  }
  .front-label {
    width: 696px;
    height: 1044px;
    display: block;
  }
  .brand-name {
    font-family: 'Oswald', sans-serif;
    font-weight: 600;
    letter-spacing: 0.5px;
  }
  .brand-name--top { fill: var(--cream); }
  .brand-name--bottom { fill: var(--almond-light); }
  .product-name {
    font-family: 'Yesteryear', cursive;
    fill: var(--cocoa);
  }
  .claim-text {
    font-family: 'Oswald', sans-serif;
    font-weight: 600;
    font-size: 7px;
    fill: var(--cream);
  }
  .process-claim {
    font-family: 'Oswald', sans-serif;
    font-weight: 600;
    font-size: 10px;
    letter-spacing: 1px;
    fill: var(--cocoa);
  }
  .flavour-name {
    font-family: 'Yesteryear', cursive;
    fill: var(--cocoa);
  }
</style>
</head>
<body>
<svg class="front-label" viewBox="0 0 480 720" xmlns="http://www.w3.org/2000/svg" aria-label="Almond Vosk front label">
  <defs>
    <clipPath id="label-outline">
      <path d="M145,0 H333 V165 C430,250 480,370 480,470 C480,620 380,718 240,718 C100,718 0,620 0,480 C0,360 70,230 145,150 Z"/>
    </clipPath>
    <linearGradient id="almond-band" x1="0" y1="0" x2="1" y2="0">
      <stop offset="0" stop-color="var(--almond-light)"/>
      <stop offset="0.55" stop-color="var(--almond)"/>
      <stop offset="1" stop-color="var(--almond-light)"/>
    </linearGradient>
    <linearGradient id="forest-band" x1="0" y1="0" x2="1" y2="0">
      <stop offset="0" stop-color="var(--forest)"/>
      <stop offset="1" stop-color="var(--forest-deep)"/>
    </linearGradient>
    <radialGradient id="splash-tone" cx="0.45" cy="0.4" r="0.75">
      <stop offset="0" stop-color="#ffffff"/>
      <stop offset="1" stop-color="#dedede"/>
    </radialGradient>
  </defs>

  <g clip-path="url(#label-outline)">
    <rect class="label-base" x="0" y="0" width="480" height="720" fill="var(--leaf-green)"/>
    <rect class="brand-band" x="145" y="0" width="188" height="320" fill="url(#forest-band)"/>
    <path class="almond-edge" d="M0,462 C40,400 95,330 145,292 L333,168 L480,80 L480,345 C440,450 330,590 190,720 L0,720 Z" fill="var(--almond-edge)"/>
    <path class="almond-band" d="M0,455 C40,395 95,325 145,288 L333,164 L480,75 L480,320 C440,430 330,570 180,720 L0,720 Z" fill="url(#almond-band)"/>
    <path class="cream-swoosh" d="M472,330 C440,440 340,580 170,700" fill="none" stroke="var(--cream)" stroke-width="10" stroke-linecap="round"/>

    <path class="milk-splash" role="img" aria-label="Splash of almond milk with droplets"
      d="M18,612 C18,566 66,536 108,544 C150,552 170,600 174,704 C112,708 52,694 30,668 C18,652 17,632 18,612 Z"
      fill="url(#splash-tone)"/>
  </g>

  <rect class="brand-badge" x="193" y="18" width="97" height="80" fill="var(--badge)"/>
  <text class="brand-name brand-name--top" x="239" y="150" font-size="24" text-anchor="middle">PLAINLY</text>
  <text class="brand-name brand-name--bottom" x="239" y="186" font-size="32" text-anchor="middle">FINE</text>

  <g class="product-title" transform="rotate(-14 230 460)">
    <text class="product-name" x="215" y="420" font-size="118" text-anchor="middle">Almond</text>
    <text class="product-name" x="250" y="515" font-size="118" text-anchor="middle">Vosk</text>
  </g>

  <g class="claims" transform="rotate(-14 255 520)">
    <circle cx="215" cy="525" r="10" fill="none" stroke="var(--cocoa)" stroke-width="1.6"/>
    <path d="M215,531 C209,526 210,519 217,517 C220,523 219,528 215,531 Z" fill="var(--cocoa)"/>
    <circle cx="252" cy="525" r="10" fill="none" stroke="var(--cocoa)" stroke-width="1.6"/>
    <rect x="248" y="520" width="8" height="10" rx="1.5" fill="var(--cocoa)"/>
    <circle cx="289" cy="525" r="10" fill="none" stroke="var(--cocoa)" stroke-width="1.6"/>
    <ellipse cx="289" cy="525" rx="5.5" ry="3" fill="var(--cocoa)"/>
    <line x1="282" y1="532" x2="296" y2="518" stroke="var(--cocoa)" stroke-width="1.6"/>
    <text class="claim-text" x="205" y="545" text-anchor="middle">RAW, SPANISH</text>
    <text class="claim-text" x="205" y="553" text-anchor="middle">ACTIVATED ALMONDS</text>
    <text class="claim-text" x="254" y="545" text-anchor="middle">100 %</text>
    <text class="claim-text" x="254" y="553" text-anchor="middle">DAIRY FREE</text>
    <text class="claim-text" x="292" y="545" text-anchor="middle">100 %</text>
    <text class="claim-text" x="292" y="553" text-anchor="middle">SOY FREE</text>
    <text class="process-claim" x="250" y="570" text-anchor="middle">COLD-PRESSED</text>
  </g>

  <g class="flavour" transform="rotate(-18 240 630)">
    <text class="flavour-name" x="240" y="630" font-size="38" text-anchor="middle">Original</text>
    <path d="M178,644 C220,643 265,641 305,636" fill="none" stroke="var(--cocoa)" stroke-width="6" stroke-linecap="round"/>
  </g>
</svg>
</body>
</html>
```